Baseball Coaching Camp for 5-14year olds needs sales campaign

Local baseball coaching camp for children is in it's 22nd year running a 4-5 week series of summer camps. Each year we use email marketing beginning around December to sell our camps to the parents to sign up their children for one or more weeks. All information about the camps can be seen on our website at https://quenmarsh.com/. In the past we have had success by changing the look of the emails each month and offering a decreasing discount as the camps get closer.

Our target market is the parents of children ages 5-14years old who like and play baseball and are interested in improving their skills in a fun environment during the Summer months.

We would like to improve the sales by developing new creative and imaginative emails for this season. We need 6 to 8 quality ads that can somehow relate to each other , these ads will be sent via our mailing list as well as used on social media. One of the owners thought it would be nice to use the "river of lanterns" theme though we are open to all ideas.
We have given you access to a dropbox link with examples of past campaigns along with artwork and images here
https://www.filetarn.com/sh/q7mwkzrbt2hfpld/BBKep-ouTanm5XoRJ148fQ2Hd?dl=0

```html
<!DOCTYPE html>
<html lang="en">
<head>
<meta charset="utf-8">
<title>Quenmarsh Baseball Academy – River of Lanterns Camp 2021</title>
<link rel="stylesheet" href="https://fonts.googleapis.com/css2?family=Oswald:wght@500;600;700&family=Roboto+Slab:wght@800;900&family=Poppins:wght@400;500;600;700&family=Libre+Baskerville&family=Roboto:wght@300&display=swap">
<style>
  :root{
    --page:#f4f4f4;
    --yellow:#ffd200;
    --pale-yellow:#fff07a;
    --orange:#f7891e;
    --red:#ee1c2e;
    --royal:#0b3db4;
    --navy:#081f6b;
    --ink:#2a2200;
    --white:#ffffff;
    --turf-dark:#1f5d12;
    --turf-light:#5fae2c;
    --social-one:#0b3db4;
    --social-two:#c83fa8;
  }
  *{box-sizing:border-box;margin:0;padding:0}
  html,body{width:1200px;height:3406px;overflow:hidden;background:var(--page)}
  .email{position:absolute;left:57px;top:51px;width:1097px}

  /* Masthead */
  .masthead{position:relative;height:307px;overflow:hidden;
    background:
      radial-gradient(ellipse 70% 55% at 50% 0%,rgba(190,235,120,.65),rgba(190,235,120,0) 70%),
      linear-gradient(180deg,#7cc447 0%,#56a42a 40%,#2f7a19 75%,#1d5410 100%)}
  .brand-mark{position:absolute;left:72px;top:82px;width:140px;height:140px;border-radius:50%;background:#1b1b1b;
    display:flex;align-items:center;justify-content:center;font:700 64px/1 'Oswald',sans-serif;color:var(--white)}
  .brand-title{position:absolute;right:44px;top:66px;text-align:right;color:var(--white);font-family:'Oswald',sans-serif;font-style:italic;text-shadow:0 4px 8px rgba(0,0,0,.45)}
  .brand-title .line1{font-weight:600;font-size:58px;letter-spacing:3px;line-height:1}
  .brand-title .line2{font-weight:700;font-size:124px;letter-spacing:6px;line-height:1;margin-top:2px}

  /* Hero */
  .hero{position:relative;height:1068px;overflow:hidden}
  .hero-photo{position:absolute;inset:0;
    background:
      radial-gradient(ellipse 38% 26% at 72% 62%,rgba(255,196,40,.95),rgba(255,196,40,0) 100%),
      radial-gradient(ellipse 30% 30% at 86% 46%,rgba(230,230,225,.75),rgba(230,230,225,0) 100%),
      radial-gradient(ellipse 55% 40% at 85% 30%,rgba(150,155,160,.55),rgba(150,155,160,0) 100%),
      linear-gradient(180deg,#15191d 0%,#23282d 35%,#3a3f44 58%,#2e6f1c 76%,#3b9523 88%,#2f7d1b 100%)}
  .kicker{position:absolute;left:40px;top:80px;font:500 108px/1 'Oswald',sans-serif;color:var(--pale-yellow);letter-spacing:-1px}
  .headline{position:absolute;left:38px;top:184px;font:900 150px/1 'Roboto Slab',serif;color:var(--orange);letter-spacing:-2px}
  .subline{position:absolute;left:40px;top:345px;font:300 54px/1 'Roboto',sans-serif;color:var(--white)}
  .year{position:absolute;left:36px;top:418px;font:700 236px/1 'Oswald',sans-serif;color:var(--yellow);letter-spacing:6px}
  .tag{position:absolute;left:38px;top:670px;width:523px;height:76px;background:var(--red);border-radius:0 14px 0 14px;color:var(--white);font:700 italic 40px/76px 'Oswald',sans-serif;text-align:center;letter-spacing:1px}

  /* Skills and offer */
  .skills{position:relative;height:1000px;overflow:hidden}
  .skills-photo{position:absolute;inset:0;
    background:
      radial-gradient(ellipse 14% 16% at 52% 28%,rgba(255,200,40,.9),rgba(255,200,40,0) 100%),
      radial-gradient(ellipse 11% 14% at 13% 17%,rgba(255,200,40,.85),rgba(255,200,40,0) 100%),
      radial-gradient(ellipse 11% 14% at 79% 15%,rgba(255,200,40,.85),rgba(255,200,40,0) 100%),
      radial-gradient(ellipse 10% 12% at 36% 14%,rgba(255,200,40,.7),rgba(255,200,40,0) 100%),
      linear-gradient(180deg,#4b4d4c 0%,#6a6a64 22%,#7f7a6c 40%,#b08c66 58%,#c89c74 78%,#b98c66 100%)}
  .skills-wave{position:absolute;inset:0}
  .skill{position:absolute;left:0;width:218px;height:68px;background:var(--yellow);border-radius:0 34px 34px 0;box-shadow:3px 3px 0 rgba(120,80,20,.55);font:600 33px/68px 'Poppins',sans-serif;color:var(--ink);padding-left:21px}
  .ages{position:absolute;left:49px;top:803px;color:var(--white)}
  .ages .label{font:400 42px/1 'Libre Baskerville',serif}
  .ages .range{font:700 100px/1 'Poppins',sans-serif;margin-top:22px;letter-spacing:-2px;white-space:nowrap}
  .offer{position:absolute;left:591px;top:652px;color:var(--white);font:400 53px/70px 'Libre Baskerville',serif;white-space:nowrap}
  .cta{position:absolute;left:575px;top:829px;width:406px;height:119px;border-radius:60px;background:var(--yellow);box-shadow:4px 6px 0 #c08a00;font:500 58px/119px 'Poppins',sans-serif;color:#111;text-align:center;text-decoration:none}

  /* Schedule */
  .schedule{background:var(--yellow);height:459px;padding:44px 0 0 31px}
  .schedule h2{display:flex;align-items:center;font:700 50px/1 'Poppins',sans-serif;color:var(--ink);letter-spacing:-.5px}
  .schedule h2::after{content:"";flex:1;height:4px;background:var(--ink);margin-left:14px;margin-top:18px}
  .schedule ul{list-style:none;margin-top:38px}
  .schedule li{font:400 33px/67px 'Poppins',sans-serif;color:#4a3800;letter-spacing:1.5px;white-space:nowrap}
  .schedule li b{font-weight:700}

  /* Contact */
  .contact{background:var(--navy);height:315px;text-align:center;color:var(--white);padding-top:48px}
  .contact .note{font:500 42px/1 'Poppins',sans-serif;letter-spacing:1.5px}
  .contact .phone{font:600 112px/1 'Oswald',sans-serif;color:var(--yellow);margin-top:36px;letter-spacing:4px}

  /* Social */
  .social{position:absolute;left:0;top:3257px;width:1200px;display:flex;justify-content:center;gap:19px}
  .social a{width:92px;height:92px;border-radius:50%;display:flex;align-items:center;justify-content:center;font:600 22px/1 'Poppins',sans-serif;color:var(--white);text-decoration:none}
  .social .one{background:var(--social-one)}
  .social .two{background:var(--social-two)}
</style>
</head>
<body>
  <main class="email">
    <header class="masthead" role="img" aria-label="Close-up of a baseball turf field">
      <div class="brand-mark">QB</div>
      <div class="brand-title">
        <div class="line1">QUENMARSH BASEBALL</div>
        <div class="line2">ACADEMY</div>
      </div>
    </header>

    <section class="hero">
      <div class="hero-photo" role="img" aria-label="Young player in a yellow jersey and batting helmet sliding on green turf"></div>
      <div class="kicker">RIVER OF</div>
      <div class="headline">LANTERNS</div>
      <div class="subline">QUENMARSH BASEBALL CAMP</div>
      <div class="year">2021</div>
      <div class="tag">OPEN FOR REGISTRATION</div>
    </section>

    <section class="skills">
      <div class="skills-photo" role="img" aria-label="Camp players in yellow shirts running the bases on a dirt infield"></div>
      <svg class="skills-wave" width="1097" height="1000" viewBox="0 0 1097 1000" aria-hidden="true">
        <path d="M0 752 C300 760 500 690 650 620 C760 568 860 540 950 575 C1020 610 1060 680 1097 735 L1097 1000 L0 1000 Z" fill="#0b3db4"/>
      </svg>
      <div class="skill" style="top:320px">Hitting</div>
      <div class="skill" style="top:415px">Pitching</div>
      <div class="skill" style="top:518px">Catching</div>
      <div class="skill" style="top:611px">Fielding</div>
      <div class="ages">
        <div class="label">Youth Ages</div>
        <div class="range">5 - 14</div>
      </div>
      <div class="offer">Sign Up Today<br>&amp; Save Money</div>
      <a class="cta" href="https://quenmarsh.com/">SIGN UP</a>
    </section>

    <section class="schedule">
      <h2>CHOOSE SCHEDULE</h2>
      <ul>
        <li><b>Week 1:</b> Dec 01 - Dec 05 at Town Park, Alderwick</li>
        <li><b>Week 2:</b> Dec 01 - Dec 05 at Fireman's Field, Brookhollow</li>
        <li><b>Week 3:</b> Dec 01 - Dec 05 at Hensley Park, Thornfield</li>
        <li><b>Week 4:</b> Dec 01 - Dec 05 at Town Park, Alderwick</li>
      </ul>
    </section>

    <section class="contact">
      <p class="note">For more queries please call us.</p>
      <p class="phone">(555) 214-7730</p>
    </section>
  </main>

  <nav class="social" aria-label="Social links">
    <a class="one" href="https://quenmarsh.com/">Like</a>
    <a class="two" href="https://quenmarsh.com/">Follow</a>
  </nav>
</body>
</html>
```